Cedarline Coalition Web Presence Design and Relaunch

Take existing web files and "clean up" for a a more presentable web landing pad.
posted presently on a site pad CSS template. at www.cedarlinecoalition.org

The site is clunky and unprofessional looking. Needs to be toned down so the urgency is conveyed, but not via a burning planet image.

Target Market(s)

Non-profit climate adaptation group targeting local government land management agencies, special districts and private landholders of natural resource properties.

Industry/Entity Type

Environment

Coding

Coded - Design and coding required

Number of Pages Required

Font styles to use
Serif
Sans Serif

Requirements
Must have
• Include current logos, aspects if content on current site www.cedarlinecoalition.org
• A regional Pacific Northwest Focus (US & Canada). Content speaking to urgency but respectful of cultural diversity and norms. Sustainability themes. Emphasis on action and implementation.
Nice to have
• link to like minded projects. Appear to future generations. Diversity in thematic areas ecological resiliency, energy, food security and infrastructure.

```html
<!DOCTYPE html>
<html lang="en">
<head>
<meta charset="utf-8">
<title>Cedarline Coalition</title>
<link href="https://fonts.googleapis.com/css2?family=Montserrat:wght@400;500;600;700&display=swap" rel="stylesheet">
<style>
:root{
  --blue:#0a8bcb;
  --blue-dark:#0679b3;
  --green:#8cc63f;
  --green-band:#a5cf4c;
  --ink:#222;
  --muted:#555;
  --footer:#262626;
  --footer-text:#ddd;
  --white:#fff;
}
*{margin:0;padding:0;box-sizing:border-box}
html,body{width:1200px;height:3663px;overflow:hidden}
body{font-family:'Montserrat',sans-serif;color:var(--ink);position:relative;background:var(--white)}
.abs{position:absolute}
.site-header{position:absolute;left:0;top:0;width:1200px;height:111px;background:var(--white)}
.brand{position:absolute;left:139px;top:30px;display:flex;align-items:center;gap:10px;font-weight:700;font-size:22px;color:var(--blue)}
.brand .dot{width:30px;height:30px;border-radius:50%;background:var(--green)}
.main-nav{position:absolute;top:44px;left:0;width:1200px;font-size:14px;font-weight:600;letter-spacing:.3px}
.main-nav a{position:absolute;text-decoration:none;color:var(--ink)}
.main-nav a.active{color:var(--blue)}
.hero{position:absolute;left:0;top:111px;width:1200px;height:488px;background:linear-gradient(100deg,#1d3a1a 0%,#3d5f2a 35%,#2c4a23 65%,#17301a 100%)}
.hero-art{position:absolute;left:160px;top:20px;width:420px;height:460px;border-radius:50% 50% 40% 40%;background:radial-gradient(circle at 55% 42%,#f6f0b0 0%,#b8cf6a 18%,rgba(90,130,60,.4) 45%,rgba(0,0,0,0) 70%)}
.hero-copy{position:absolute;right:142px;top:155px;width:460px;text-align:right;color:var(--white)}
.hero-copy .eyebrow{font-size:14px;font-weight:600;letter-spacing:.4px}
.hero-copy h1{font-size:21px;font-weight:700;margin-top:8px;letter-spacing:.3px}
.hero-copy p{font-size:14px;line-height:21.5px;margin-top:12px}
.scroll-down{position:absolute;left:576px;top:576px;width:48px;height:48px;border-radius:50%;background:var(--white);display:flex;align-items:center;justify-content:center}
.section-title{position:absolute;left:0;width:1200px;text-align:center;font-size:30px;font-weight:700}
.section-title .b{color:var(--blue)}
.section-title .g{color:var(--green)}
.rule{position:absolute;left:565px;width:70px;height:2px;background:linear-gradient(90deg,var(--blue) 0 33%,var(--green) 33% 67%,var(--blue) 67%)}
.card{position:absolute;width:223px;text-align:center}
.card .photo{width:223px;height:189px}
.card .icon{position:absolute;left:75px;width:72px;height:72px;border-radius:50%;background:var(--white);box-shadow:0 2px 8px rgba(0,0,0,.12);display:flex;align-items:center;justify-content:center}
.card.active .icon{background:var(--blue)}
.card h3{font-size:14.5px;font-weight:700;margin-top:51px;letter-spacing:.2px}
.card.active h3{color:var(--blue)}
.card p{font-size:12.5px;line-height:19px;color:var(--muted);margin-top:4px;padding:0 8px}
.card .base{position:absolute;left:0;width:223px;height:4px;background:#eef0e2}
.card.active .base{background:var(--blue)}
.doing{position:absolute;left:0;top:1311px;width:1200px;height:407px;background:var(--blue);color:var(--white);text-align:center}
.doing h2{position:absolute;top:70px;width:100%;font-size:30px;font-weight:700}
.doing .rule{top:117px;background:linear-gradient(90deg,#fff 0 33%,var(--green) 33% 67%,#fff 67%)}
.doing .lead{position:absolute;top:140px;left:200px;width:800px;font-size:18px;line-height:28px}
.doing .body{position:absolute;top:205px;left:190px;width:820px;font-size:12.5px;line-height:19px}
.btn{position:absolute;height:33px;border-radius:17px;font-size:12.5px;font-weight:700;display:flex;align-items:center;justify-content:center;letter-spacing:.2px}
.btn-white{background:var(--white);color:var(--blue)}
.btn-solid{background:var(--blue);color:var(--white)}
.btn-outline{border:1.5px solid var(--blue);color:var(--blue);background:var(--white)}
.stat{position:absolute;width:220px;text-align:center}
.stat .ring{margin:0 auto;width:102px;height:102px;border-radius:50%;border:6px solid #f3f3f3;display:flex;align-items:center;justify-content:center}
.stat .num{font-size:29px;font-weight:700;margin-top:16px}
.stat .lbl{font-size:14px;color:var(--muted);margin-top:2px}
.blue{color:var(--blue)}.green{color:var(--green)}
.recent{position:absolute;left:0;top:2099px;width:1200px;height:568px;background:var(--green-band)}
.tile{position:absolute;color:var(--white);text-align:center}
.tile .cap{position:absolute;left:0;bottom:18px;width:100%}
.tile strong{display:block;font-size:15px;font-weight:700}
.tile span{font-size:12.5px}
.savings-art{position:absolute;left:107px;top:2730px;width:412px;height:448px;border-radius:50%;background:radial-gradient(circle at 50% 60%,#5dbf7a 0%,#2f8f4a 40%,#a8d8a8 60%,rgba(255,255,255,0) 72%)}
.savings h2{position:absolute;left:596px;top:2776px;font-size:30px;font-weight:700}
.meter{position:absolute;left:589px;width:425px}
.meter .row{display:flex;justify-content:space-between;font-size:16px;font-weight:700;padding:0 12px 0 15px}
.meter .track{margin-top:10px;height:15px;border-radius:8px;border:1.5px solid #ccc;background:#f5f5f5;overflow:hidden}
.meter .fill{height:100%;border-radius:8px}
.site-footer{position:absolute;left:0;top:3246px;width:1200px;height:373px;background:var(--footer);color:var(--footer-text)}
.site-footer h4{position:absolute;font-size:16px;font-weight:700;color:var(--white);letter-spacing:.3px}
.site-footer .uline{position:absolute;width:36px;height:2px;background:var(--green)}
.links{position:absolute;left:141px;top:130px;list-style:none;font-size:14px;line-height:28.2px}
.contact-item{position:absolute;left:306px;display:flex;gap:14px;font-size:14px;line-height:21px}
.contact-item .ic{width:34px;height:34px;border-radius:50%;background:var(--blue);display:flex;align-items:center;justify-content:center;flex:none}
.contact-item small{font-size:12px;display:block}
.contact-item .name{color:var(--blue);font-weight:600}
.map{position:absolute;left:617px;top:131px;width:233px;height:166px;background:linear-gradient(135deg,#eef1f4,#dfe6ec)}
.footer-brand{position:absolute;left:910px;top:160px;display:flex;align-items:center;gap:10px;font-size:20px;font-weight:700;color:var(--blue)}
.footer-brand .dot{width:28px;height:28px;border-radius:50%;background:var(--green)}
.copybar{position:absolute;left:0;top:3619px;width:1200px;height:44px;background:var(--green);color:var(--white);font-size:13px}
.copybar p{position:absolute;left:142px;top:14px}
.social{position:absolute;right:142px;top:13px;display:flex;gap:16px}
.social i{display:block;width:16px;height:16px;border-radius:50%;background:rgba(255,255,255,.85)}
</style>
</head>
<body>

<header class="site-header">
  <div class="brand"><span class="dot"></span>Cedarline Coalition</div>
  <nav class="main-nav">
    <a class="active" style="left:758px">HOME</a>
    <a style="left:845px">ABOUT US</a>
    <a style="left:961px">CONTACT US</a>
  </nav>
</header>

<section class="hero">
  <div class="hero-art" role="img" aria-label="Hand holding a glowing light bulb ringed by clean energy icons over green foliage"></div>
  <div class="hero-copy">
    <div class="eyebrow">CLIMATE ADAPTATION</div>
    <h1>IMPLEMENTING CLIMATE STRATEGIES</h1>
    <p>Dedicated to taking action the Cedarline Coalition was created to help bring adaption strategies to life. Working with local communities we are committed to implementing strategies that will sustain communities throughout the Pacific Northwest for generations to come.</p>
  </div>
</section>
<div class="scroll-down"><svg width="14" height="14" viewBox="0 0 14 14"><path d="M7 2v9M3.5 7.5 7 11l3.5-3.5" stroke="#8cc63f" stroke-width="2" fill="none"/></svg></div>

<h2 class="section-title" style="top:680px"><span class="b">FEATURED</span> <span class="g">PROJECTS</span></h2>
<div class="rule" style="top:731px"></div>

<article class="card" style="left:141px;top:783px">
  <div class="photo" role="img" aria-label="Volunteers in green shirts working outdoors" style="background:linear-gradient(160deg,#6f9a3c,#3f6a2a)"></div>
  <div class="icon" style="top:153px"><svg width="32" height="28" viewBox="0 0 32 28" fill="none" stroke="#0a8bcb" stroke-width="1.6"><rect x="3" y="5" width="24" height="18" rx="2"/><path d="M8 11h14M8 15h14M8 19h8"/></svg></div>
  <h3>ADAPTATION PLANS</h3>
  <p>Communities throughout the region have adopted plans to to address our changing climate. Many more are in the process of developing plans. We are here to help these communities with the hard work- implementing those plans.</p>
  <div class="base" style="top:440px"></div>
</article>

<article class="card active" style="left:372px;top:769px">
  <div class="photo" role="img" aria-label="Aerial view of a winding river through wetlands" style="background:linear-gradient(160deg,#a88f4a,#2d6b9a 55%,#8c7a3a)"></div>
  <div class="icon" style="top:153px"><svg width="34" height="32" viewBox="0 0 34 32" fill="none" stroke="#fff" stroke-width="2"><path d="M17 4l6 10M23 14l-4-1M11 14l6-10M11 14l4-1M7 22h12M7 22l3 4M27 22l-6 6M27 22l-1-4"/></svg></div>
  <h3>ON THE GROUND</h3>
  <p>The Alliance is familiar and growing throughout the region. Presently our work has us on the ground in keystone watersheds in the Cascade, Willamette, Columbia and Boise basin watersheds.</p>
  <div class="base" style="top:439px"></div>
</article>

<article class="card" style="left:604px;top:783px">
  <div class="photo" role="img" aria-label="Lake with cliffs and sky" style="background:linear-gradient(180deg,#9cc3e6,#6f8fae 45%,#a27b63)"></div>
  <div class="icon" style="top:153px"><svg width="24" height="32" viewBox="0 0 24 32" fill="none" stroke="#0a8bcb" stroke-width="1.6"><path d="M12 3a8 8 0 0 0-5 14v5h10v-5A8 8 0 0 0 12 3zM8 26h8M9 29h6"/></svg></div>
  <h3>ECOLOGICAL RESILIENCE</h3>
  <p>To endure change Communities need to keep their watersheds functioning. Our network or professionals have decades of experience understanding &amp; implementing conservation and restoration strategies.</p>
  <div class="base" style="top:440px"></div>
</article>

<article class="card" style="left:836px;top:783px">
  <div class="photo" role="img" aria-label="Green grain field under a blue sky" style="background:linear-gradient(180deg,#8fb8e0 0%,#cfe2ef 35%,#7fa23a 45%,#6c8d2e)"></div>
  <div class="icon" style="top:153px"><svg width="34" height="34" viewBox="0 0 34 34" fill="none" stroke="#0a8bcb" stroke-width="1.6"><circle cx="17" cy="17" r="9"/><path d="M18 11l-4 7h5l-3 6M17 2v4M17 28v4M2 17h4M28 17h4"/></svg></div>
  <h3>ENERGY AND FOOD</h3>
  <p>Security of community food and energy have, and always will be, an essential component of how communities sustain themselves. Beyond the the ecological context managing a minimizing our resource demands will be essential.</p>
  <div class="base" style="top:440px"></div>
</article>

<section class="doing">
  <h2>WHAT WE ARE DOING ?</h2>
  <div class="rule"></div>
  <p class="lead">Lorem Ipsum is simply dummy text of the printing and typesetting industry. Lorem Ipsum has been the industry's standard dummy text ever since the 1500s.</p>
  <p class="body">It is a long established fact that a reader will be distracted by the readable content of a page when looking at its layout. The point of using Lorem Ipsum is that it has a more-or-less normal distribution of letters, as opposed to using 'Content here, content here', making it look like readable English. Many desktop publishing packages and web page editors now use Lorem Ipsum as their default model text, and a search for 'lorem ipsum' will uncover many web sites still in their infancy.</p>
  <div class="btn btn-white" style="left:511px;top:302px;width:177px">CONTACT US TODAY</div>
</section>

<div class="stat" style="left:142px;top:1797px">
  <div class="ring"><svg width="34" height="40" viewBox="0 0 34 40" fill="none" stroke="#0a8bcb" stroke-width="1.8"><rect x="4" y="6" width="26" height="31" rx="2"/><rect x="11" y="2" width="12" height="7" rx="1"/><circle cx="17" cy="22" r="7"/><path d="M13.5 22l2.5 2.5 4.5-5"/></svg></div>
  <div class="num blue">250+</div><div class="lbl">Projects Completed</div>
</div>
<div class="stat" style="left:373px;top:1797px">
  <div class="ring"><svg width="34" height="40" viewBox="0 0 34 40" fill="none" stroke="#8cc63f" stroke-width="1.8"><circle cx="17" cy="13" r="9"/><path d="M17 8v10M14 10h5M14 16h5M3 30l8-4h10l6-4M3 36l10 0 14-8"/></svg></div>
  <div class="num green">300+</div><div class="lbl">Donations</div>
</div>
<div class="stat" style="left:604px;top:1797px">
  <div class="ring"><svg width="40" height="40" viewBox="0 0 40 40" fill="none" stroke="#0a8bcb" stroke-width="1.6"><circle cx="20" cy="7" r="3"/><circle cx="7" cy="20" r="3"/><circle cx="33" cy="20" r="3"/><circle cx="20" cy="33" r="3"/><path d="M24 9l6 7M10 16l6-7M30 24l-6 7M16 31l-6-7"/></svg></div>
  <div class="num blue">17+</div><div class="lbl">Communities Engaged</div>
</div>
<div class="stat" style="left:837px;top:1797px">
  <div class="ring"><svg width="40" height="36" viewBox="0 0 40 36" fill="none" stroke="#8cc63f" stroke-width="1.6"><circle cx="20" cy="9" r="4"/><circle cx="10" cy="14" r="3"/><circle cx="30" cy="14" r="3"/><path d="M12 24c0-5 4-8 8-8s8 3 8 8M3 22l7 8h20l7-8"/></svg></div>
  <div class="num green">70+</div><div class="lbl">Volunteers</div>
</div>
<div class="btn btn-solid" style="left:433px;top:1993px;width:141px">JOIN US TODAY</div>
<div class="btn btn-outline" style="left:590px;top:1993px;width:177px">CONTACT US TODAY</div>

<section class="recent">
  <h2 class="section-title" style="top:70px"><span class="b">RECENT</span> <span style="color:#fff">WORK</span></h2>
  <div class="rule" style="top:120px;background:linear-gradient(90deg,#fff 0 33%,var(--blue) 33% 67%,#fff 67%)"></div>
  <div class="tile" style="left:141px;top:155px;width:301px;height:341px;background:linear-gradient(180deg,#a9c3cf 0%,#f0c070 45%,#5a4a2a 75%,#2a2418)" role="img" aria-label="Wind turbines on hills at sunset">
    <div class="cap"><strong>Energy</strong><span>Investing in clean energy</span></div>
  </div>
  <div class="tile" style="left:449px;top:155px;width:300px;height:166px;background:linear-gradient(160deg,#6b7d3a,#c9b36a 50%,#4f6b2a)" role="img" aria-label="Hands holding harvested rice grain">
    <div class="cap"><strong>Food Security</strong><span>Retooling agriculture/span</span></div>
  </div>
  <div class="tile" style="left:449px;top:329px;width:300px;height:167px;background:linear-gradient(160deg,#3a2a2a,#8a4a3a 50%,#2c3a2a)" role="img" aria-label="Aerial view of a rugged landscape">
    <div class="cap"><strong>Ecological Resilience</strong><span>Environmental Progress</span></div>
  </div>
  <div class="tile" style="left:758px;top:155px;width:300px;height:341px;background:linear-gradient(180deg,#3b4a3a,#6a7060 40%,#3a2e28 80%,#1e1a16)" role="img" aria-label="Hand holding a phone showing a forest road">
    <div class="cap"><strong>Infrastructure</strong><span>Lorem ipsum dolor sit</span></div>
  </div>
</section>

<div class="savings-art" role="img" aria-label="Illustrated globe topped with forest, mountains, rainbow and sun"></div>
<section class="savings">
  <h2><span class="b">THINK GREEN !</span> <span class="g">SAVE MONEY</span></h2>
  <div class="meter" style="top:2870px"><div class="row blue"><span>Clean Water</span><span>98%</span></div><div class="track"><div class="fill" style="width:98%;background:linear-gradient(90deg,#1d88c9,#5cc0ef,#1d88c9)"></div></div></div>
  <div class="meter" style="top:2942px"><div class="row" style="color:#6a8a2e"><span>Forest Rescue</span><span>56%</span></div><div class="track"><div class="fill" style="width:63%;background:linear-gradient(90deg,#2e5a1e,#6e9a3a,#2e5a1e)"></div></div></div>
  <div class="meter" style="top:3015px"><div class="row green"><span>Agriculture</span><span>77%</span></div><div class="track"><div class="fill" style="width:84%;background:linear-gradient(90deg,#2f7a22,#6cbf3a,#2f7a22)"></div></div></div>
  <div class="meter" style="top:3087px"><div class="row blue"><span>Alternative Energy</span><span>84%</span></div><div class="track"><div class="fill" style="width:92%;background:linear-gradient(90deg,#56b4e3,#a6dcf3,#56b4e3)"></div></div></div>
</section>

<footer class="site-footer">
  <h4 style="left:141px;top:73px">QUICK LINKS</h4><div class="uline" style="left:141px;top:101px"></div>
  <ul class="links"><li>Home</li><li>About Us</li><li>Causes</li><li>Testimonial</li><li>Events</li><li>Contact Us</li></ul>

  <h4 style="left:310px;top:73px">CONTACT DETAILS</h4><div class="uline" style="left:310px;top:101px"></div>
  <div class="contact-item" style="top:128px">
    <div class="ic"><svg width="14" height="18" viewBox="0 0 14 18"><path d="M7 1a6 6 0 0 0-6 6c0 4.5 6 10 6 10s6-5.5 6-10a6 6 0 0 0-6-6z" fill="#fff"/><circle cx="7" cy="7" r="2.2" fill="#0a8bcb"/></svg></div>
    <div><span class="name">Cedarline Coalition</span><br>418 Alder Bend Rd<br>Riverton WA 98000</div>
  </div>
  <div class="contact-item" style="top:210px">
    <div class="ic"><svg width="16" height="16" viewBox="0 0 16 16"><path d="M3 1l3 3-1.5 2a9 9 0 0 0 5.5 5.5L12 10l3 3-2 2C7 15 1 9 1 3z" fill="#fff"/></svg></div>
    <div><small>Call Us:</small>360-555-0148</div>
  </div>
  <div class="contact-item" style="top:264px">
    <div class="ic"><svg width="16" height="12" viewBox="0 0 16 12"><rect x="0.5" y="0.5" width="15" height="11" rx="1" fill="#fff"/><path d="M1 1l7 6 7-6" stroke="#0a8bcb" fill="none"/></svg></div>
    <div><small>Mail Us:</small>info@cedarlinecoalition.org</div>
  </div>

  <h4 style="left:617px;top:73px">LOCATION MAP</h4><div class="uline" style="left:617px;top:101px"></div>
  <div class="map" role="img" aria-label="Street map showing the office location"></div>

  <div class="footer-brand"><span class="dot"></span>Cedarline Coalition</div>
</footer>

<div class="copybar">
  <p>Copyright © 2020 Cedarline Coalition. All Rights Reserved.</p>
  <div class="social"><i></i><i></i><i></i><i></i></div>
</div>

</body>
</html>
```